Hitech firm looking for Email header graphics for a new post purchase communication plan

This new communication plan is to get our new customers to feel part of our innovative and hi-tech family. We want to bring professionalism with a cool/fun approach.

We need 3 separate designs for 3 different post purchase email communications:
Email 1: sent immediately after purchase - Welcome & thank you for your order
Email 2: Shipment & tracking notification - Your product has shipped
Email 3: License activation code and instructions - Your license is ready

Our customer service and support team have a 98% customer satisfaction rating, we're good at what we do. For this we wanted to bring those people to life from behind the phone and show our customers who they are actually speaking to. the photos attached are our own employees not stock images, the ones that get rated Awesome, Amazing, life savers and more from existing customers. We want to find a creative way to show they are our guys and they have a sense of humor as well as phenomenal knowledge that saves companies bacon each and every day.

If you can think of a good way to incorporate that in imagery would be great - e.g.names? length of service or a quirky caption e.g. "Backup Wizard Doug" / "Recovery Viking Raul" "Ransomware Pirate Omar".

We are open to colour imagery or black/white with a colour pop in red or blue, please see our website www.velbrooke-demo.net for our colour style. Our email header template is attached so you can see where the imagery should go.

Also we have created some speech bubbles to include on imagery. feel free to redesign these if you see fit. the wording should not be changed. Colours used are our corporate do not include new colours but feel free to remove the amount of colour if you wish. They do not have to all be used. 6 to choose from.

Target Market(s)

IT Pros / New customers to Velbrooke

Industry/Entity Type

Information Technology

Font styles to use
Sans Serif

Colors

Designer to choose colors to be used in the design.

Requirements
Must have
• 3 separate email header images
Nice to have
• I'd like to see something that identifies these are real Velbrooke employees for example: "just a few members of the Velbrooke support team" not that exactly I'll leave the creatives to you!
Should not have
• No logo required on this image

```html
<!DOCTYPE html>
<html lang="en">
<head>
<meta charset="utf-8">
<title>Post Purchase Email Headers</title>
<link href="https://fonts.googleapis.com/css2?family=Fira+Sans+Condensed:ital,wght@0,400;0,600;1,700&display=swap" rel="stylesheet">
<style>
  :root {
    --canvas: #ffffff;
    --teal: #00b2bc;
    --white: #ffffff;
    --bubble-red: #e0163f;
    --bubble-teal: #17a4b6;
    --photo-dark: #1f1f22;
    --photo-mid: #3a3536;
  }
  html, body {
    margin: 0;
    padding: 0;
    width: 1200px;
    height: 900px;
    overflow: hidden;
    background: var(--canvas);
    font-family: "Fira Sans Condensed", sans-serif;
  }
  .canvas {
    position: relative;
    width: 1200px;
    height: 900px;
  }
  .email-header {
    position: absolute;
    width: 546px;
    height: 252px;
    background: var(--teal);
    overflow: hidden;
  }
  .email-header--welcome { left: 36px; top: 206px; }
  .email-header--shipped { left: 612px; top: 206px; }
  .email-header--activation { left: 324px; top: 488px; }

  .header-copy {
    position: absolute;
    left: 0;
    top: 0;
    width: 248px;
    height: 100%;
    text-align: center;
    color: var(--white);
  }
  .headline {
    position: absolute;
    left: 0;
    right: 0;
    top: 60px;
    margin: 0;
    font-weight: 600;
    font-size: 31px;
    line-height: 37px;
    letter-spacing: -0.2px;
  }
  .subline {
    position: absolute;
    left: 0;
    right: 0;
    top: 164px;
    margin: 0;
    font-weight: 400;
    font-size: 19px;
    line-height: 24px;
  }
  .team-photo {
    position: absolute;
    left: 0;
    top: 0;
    width: 546px;
    height: 252px;
  }
  .bubble-text {
    font-family: "Fira Sans Condensed", sans-serif;
    font-style: italic;
    font-weight: 700;
    font-size: 11.5px;
    fill: var(--white);
  }
</style>
</head>
<body>
<div class="canvas">

  <section class="email-header email-header--welcome">
    <div class="header-copy">
      <h2 class="headline">Welcome<br>To The Team!!!</h2>
      <p class="subline">are you ready to start?</p>
    </div>
    <svg class="team-photo" viewBox="0 0 546 252" xmlns="http://www.w3.org/2000/svg">
      <defs>
        <linearGradient id="photoWelcome" x1="0" y1="0" x2="1" y2="1">
          <stop offset="0" stop-color="#2b2627"/>
          <stop offset="0.45" stop-color="#4a3a3a"/>
          <stop offset="0.75" stop-color="#7a2030"/>
          <stop offset="1" stop-color="#1f1f22"/>
        </linearGradient>
      </defs>
      <polygon points="318,0 546,0 546,252 226,252" fill="url(#photoWelcome)" role="img" aria-label="Photo of support team members in party costumes with feather boas, hats and masks"/>
      <g class="speech-bubble">
        <path d="M418 96 L446 132 L436 102 Z" fill="var(--bubble-red)"/>
        <ellipse cx="452" cy="102" rx="48" ry="36" fill="var(--bubble-red)"/>
        <text class="bubble-text" text-anchor="middle" x="452"><tspan x="452" y="90">We Put the</tspan><tspan x="452" y="105">ZING</tspan><tspan x="452" y="120">in AMAZING!</tspan></text>
      </g>
    </svg>
  </section>

  <section class="email-header email-header--shipped">
    <div class="header-copy">
      <h2 class="headline">Your Product<br>Has Shipped!!!</h2>
      <p class="subline">let the good times roll...</p>
    </div>
    <svg class="team-photo" viewBox="0 0 546 252" xmlns="http://www.w3.org/2000/svg">
      <defs>
        <linearGradient id="photoShipped" x1="0" y1="0" x2="1" y2="1">
          <stop offset="0" stop-color="#3a3032"/>
          <stop offset="0.5" stop-color="#2a2a30"/>
          <stop offset="0.8" stop-color="#8a4a22"/>
          <stop offset="1" stop-color="#1f1f22"/>
        </linearGradient>
      </defs>
      <polygon points="318,0 546,0 546,252 226,252" fill="url(#photoShipped)" role="img" aria-label="Photo of support team members wearing a wizard hat, viking helmet with orange beard and superhero mask"/>
      <g class="speech-bubble">
        <path d="M400 196 L388 218 L418 196 Z" fill="var(--bubble-red)"/>
        <ellipse cx="385" cy="170" rx="49" ry="34" fill="var(--bubble-red)"/>
        <text class="bubble-text" text-anchor="middle"><tspan x="385" y="158">I Don’t Do</tspan><tspan x="385" y="173">Average, I do</tspan><tspan x="385" y="188">AWESOME!</tspan></text>
      </g>
    </svg>
  </section>

  <section class="email-header email-header--activation">
    <div class="header-copy">
      <h2 class="headline">Your Activation<br>Is Here!!!</h2>
      <p class="subline">you’re good to go...</p>
    </div>
    <svg class="team-photo" viewBox="0 0 546 252" xmlns="http://www.w3.org/2000/svg">
      <defs>
        <linearGradient id="photoActivation" x1="0" y1="0" x2="1" y2="1">
          <stop offset="0" stop-color="#3b3330"/>
          <stop offset="0.4" stop-color="#6a4a2a"/>
          <stop offset="0.7" stop-color="#5a2a5a"/>
          <stop offset="1" stop-color="#1f1f22"/>
        </linearGradient>
      </defs>
      <polygon points="318,0 546,0 546,252 226,252" fill="url(#photoActivation)" role="img" aria-label="Photo of support team members in straw hats, sombrero, tiara and crown with colourful feather boas"/>
      <g class="speech-bubble">
        <path d="M352 126 L340 110 L368 120 Z" fill="var(--bubble-teal)"/>
        <ellipse cx="378" cy="148" rx="48" ry="34" fill="var(--bubble-teal)"/>
        <text class="bubble-text" text-anchor="middle"><tspan x="378" y="137">Delighting</tspan><tspan x="378" y="151">customers is my</tspan><tspan x="378" y="165">SUPERPOWER</tspan></text>
      </g>
    </svg>
  </section>

</div>
</body>
</html>
```